Sexy stockings - 1 creative web page design needed!

We need a design for the main home page of our company 'Calloway Hosiery'. Out company sells stockings for women in Australia and this will be an online shopping site.

I have mocked up an example showing the type of layout and text that is required:
http://www.callowayhosiery.example.au

The design should have the same menu and text as shown in the example. A slider will be positioned in the middle of the page promoting certain styles.

The page currently has a width of 800px.

What I am looking for is some genuine design flare. Good use of fonts, stylish menu and interesting background. Also please note, this is the will be the home page so please keep text to a minimum.

An example of stylish menus can be seen here: (See 22, 26, 41)
http://brightpalette.example.com/design-showcase-inspiration/50-stylish-navigation-menus-for-design-inspiration/

An example of creative footers:
http://www.trelvomag.example.com/2009/01/40-nice-and-creative-website-footer-designs/

(See 22, 26, 41)

Update: I would like a banner picture at the top with the logo and title overlaid. Also some areas where I could advertise specials and 1 day delivery in the Metro area.

Only one page is required to be designed. No coding of links, slider etc is needed.

The deliverable will be one photoshop project file.
Updates

So far the designs submitted have not been very creative. I am not interested in a plain design where you have just copy and pasted the pictures I  have supplied and changed the background colour - I could do this myself in Photoshop. What I am looking for is some genuine design flare. Good use of fonts, stylish menu and interesting background.

Also note - this is a home page, so there should be minimal text. 

Once a quality design has been submitted, I will guarantee this project.

Reason: I have extended the deadline in order for designers to submit their new designs for the following update to the brief: I have decided a banner picture at the top with the logo and title overlaid would look great. Also can I have some areas on the page where I could advertise specials and 1 day delivery in the Metro area.

I have now guaranteed the project.

Target Market(s)

We are marketing this product to the sophisticated professional woman.

Industry/Entity Type

Online Shopping

Requirements
Must have
• Must have the subtitle - "Signature Italian Stockings"

Logo picture incorporated somewhere on page. (Do not include "Sheer Silky Stockings" from packaging.)

The style of the webpage should be consistent with the packaging.

Please see the attached files.
Nice to have
• A creative background pattern - maybe incorporate the logo.
Should not have
• I am looking for a CREATIVE design, do not submit a design that has is just the supplied pictures copy and pasted in a different layout. (I could easily do that myself).

```html
<!DOCTYPE html>
<html lang="en">
<head>
<meta charset="utf-8">
<title>Calloway Hosiery – Signature Italian Stockings</title>
<link href="https://fonts.googleapis.com/css2?family=Cormorant+Garamond:wght@400;500&family=Gelasio:wght@400;700&family=Arimo:wght@400;700&display=swap" rel="stylesheet">
<style>
  :root {
    --page-bg: #3d3d40;
    --page-bg-dark: #2c2c2f;
    --pattern-line: rgba(255,255,255,.045);
    --pink: #e9b7bd;
    --pink-light: #f6d6da;
    --pink-deep: #d9a1a8;
    --ink: #4a4a4c;
    --ink-soft: #5d5d60;
    --white: #ffffff;
  }
  * { box-sizing: border-box; margin: 0; padding: 0; }
  html, body { width: 1200px; height: 749px; overflow: hidden; }
  body {
    position: relative;
    background: var(--page-bg);
    font-family: "Gelasio", Georgia, serif;
  }
  .backdrop-pattern {
    position: absolute; inset: 0;
    background:
      repeating-linear-gradient(0deg, var(--pattern-line) 0 1px, transparent 1px 12px),
      repeating-linear-gradient(90deg, transparent 0 30px, rgba(0,0,0,.06) 30px 31px),
      linear-gradient(90deg, var(--page-bg-dark) 0%, #48484b 50%, var(--page-bg-dark) 100%);
  }
  .site {
    position: absolute; left: 120px; top: 0; width: 960px; height: 656px;
    overflow: hidden;
    box-shadow: 0 0 18px rgba(0,0,0,.55);
  }
  .hero-photo {
    position: absolute; inset: 0;
    background:
      radial-gradient(ellipse 220px 260px at 800px 110px, #e8cdb8 0%, rgba(232,205,184,0) 70%),
      radial-gradient(ellipse 260px 200px at 470px 120px, #8c3d44 0%, rgba(140,61,68,0) 75%),
      linear-gradient(90deg, #2e3a26 0%, #4a3028 28%, #6b2f36 48%, #3a2422 68%, #5c4a3c 82%, #2a2320 100%);
  }
  .hero-photo::after {
    content: ""; position: absolute; inset: 0;
    background: linear-gradient(180deg, rgba(0,0,0,0) 40%, rgba(20,14,14,.35) 100%);
  }

  /* brand */
  .brand { position: absolute; left: 34px; top: 12px; width: 180px; text-align: center; }
  .brand-dot {
    display: block; width: 86px; height: 86px; margin: 0 auto 10px;
    border-radius: 50%; background: var(--pink);
  }
  .brand-name {
    font-family: "Cormorant Garamond", Georgia, serif; font-weight: 400;
    font-size: 46px; line-height: 44px; color: var(--white); letter-spacing: 1px;
  }
  .brand-tagline {
    font-family: "Arimo", Arial, sans-serif; font-size: 8.5px; color: var(--pink-light);
    letter-spacing: 1.4px; margin-top: 2px; white-space: nowrap;
  }

  /* top bar */
  .topbar {
    position: absolute; left: 236px; top: 40px; width: 724px; height: 24px;
    background: linear-gradient(180deg, var(--pink-light), var(--pink-deep));
  }
  .cart {
    position: absolute; right: 0; top: 0; height: 24px;
    display: flex; align-items: center; font-family: "Arimo", Arial, sans-serif;
    font-size: 11.5px; color: var(--ink);
  }
  .cart-count { display: flex; align-items: center; gap: 6px; margin-right: 14px; }
  .cart-view {
    height: 24px; line-height: 24px; padding: 0 8px; font-weight: 700;
    background: #fbe6e8; border-left: 1px solid var(--pink-deep);
  }

  /* main navigation */
  .main-nav { position: absolute; left: 250px; top: 40px; width: 400px; height: 92px; }
  .nav-ribbon { position: absolute; left: 0; top: 0; }
  .nav-link {
    position: absolute; top: 38px; font-size: 13.5px; color: var(--white);
    text-transform: uppercase; letter-spacing: .3px; text-decoration: none; white-space: nowrap;
  }
  .nav-link.is-active { left: 2px; width: 92px; text-align: center; color: var(--pink); font-size: 12.5px; }
  .nav-news { left: 145px; }
  .nav-about { left: 242px; }

  /* specials ribbon */
  .specials { position: absolute; left: 22px; top: 228px; width: 208px; height: 396px; }
  .specials svg { position: absolute; inset: 0; }
  .specials-title {
    position: absolute; top: 16px; left: 0; width: 100%; text-align: center;
    color: var(--pink); font-size: 15.5px; font-weight: 400; line-height: 20px;
    letter-spacing: 0; white-space: nowrap;
  }
  .specials-list { position: absolute; top: 56px; left: 0; width: 100%; list-style: none; text-align: center; }
  .specials-list li {
    color: var(--white); font-size: 15px; line-height: 18px; height: 70px;
    text-shadow: 0 1px 2px rgba(0,0,0,.6);
  }

  /* slider */
  .slider {
    position: absolute; left: 250px; top: 228px; width: 633px; height: 401px;
    background: rgba(255,255,255,.82); border: 2px solid var(--pink);
  }
  .slide-photo {
    position: absolute; inset: 0;
    background:
      radial-gradient(ellipse 110px 190px at 290px 210px, rgba(40,34,34,.55) 0%, rgba(40,34,34,0) 75%),
      linear-gradient(90deg, rgba(235,228,226,.7) 0%, rgba(250,246,245,.4) 50%, rgba(225,218,216,.7) 100%);
  }
  .slider-arrow { position: absolute; top: 168px; width: 29px; height: 30px; }
  .slider-arrow.prev { left: 0; }
  .slider-arrow.next { right: 0; }
  .slider-dots { position: absolute; left: 10px; bottom: 8px; display: flex; gap: 5px; }
  .slider-dots span { width: 8px; height: 8px; border: 1px solid var(--pink-deep); background: #fff; }
  .slider-dots span.is-current { background: var(--pink-deep); }

  /* footer */
  .site-footer {
    position: absolute; left: 0; top: 656px; width: 1200px; height: 93px;
    background: linear-gradient(180deg, #f0c4c8 0%, #f7d6d9 60%, #f3c9cd 100%);
    border-top: 3px solid #fbe3e5;
    box-shadow: inset 0 1px 0 var(--pink-deep);
  }
  .delivery {
    position: absolute; left: 181px; top: 24px; font-weight: 700; font-size: 14.5px;
    line-height: 19px; color: var(--ink); letter-spacing: .4px;
  }
  .footer-links {
    position: absolute; top: 22px; list-style: none; padding-left: 10px;
    border-left: 1px solid #b9989c; height: 54px;
    font-family: "Arimo", Arial, sans-serif; font-size: 12.5px; line-height: 19px;
  }
  .footer-links a { color: var(--ink-soft); text-decoration: none; }
  .links-site { left: 366px; }
  .links-shop { left: 470px; }
  .links-info { left: 588px; }
  .footer-brand {
    position: absolute; right: 142px; top: 24px; text-align: right;
    font-family: "Arimo", Arial, sans-serif; color: var(--ink-soft); font-weight: 700;
  }
  .footer-brand .name { font-size: 12px; line-height: 13px; }
  .footer-brand .tagline { font-size: 9.5px; line-height: 11px; }
  .footer-brand .copyright { font-size: 9.5px; margin-top: 14px; }
</style>
</head>
<body>
  <div class="backdrop-pattern" role="img" aria-label="Dark grey background with a faint repeating brand-name pattern"></div>

  <div class="site">
    <div class="hero-photo" role="img" aria-label="Banner photograph of a woman in lingerie and stockings reclining on a red velvet chair before ornate wallpaper and ferns"></div>

    <div class="brand">
      <span class="brand-dot"></span>
      <div class="brand-name">calloway</div>
      <div class="brand-tagline">Signature Italian Stockings</div>
    </div>

    <div class="topbar">
      <div class="cart">
        <span class="cart-count">
          <svg width="16" height="13" viewBox="0 0 16 13" aria-hidden="true">
            <path d="M0 1h3l2 7h8l2-5H4" fill="none" stroke="#4a4a4c" stroke-width="1.5"/>
            <circle cx="6" cy="11" r="1.3" fill="#4a4a4c"/><circle cx="12" cy="11" r="1.3" fill="#4a4a4c"/>
          </svg>
          0 Items
        </span>
        <span class="cart-view">View Cart</span>
      </div>
    </div>

    <nav class="main-nav">
      <svg class="nav-ribbon" width="96" height="92" viewBox="0 0 96 92" aria-hidden="true">
        <defs>
          <linearGradient id="navTab" x1="0" y1="0" x2="0" y2="1">
            <stop offset="0" stop-color="#6a6a6e"/><stop offset="1" stop-color="#3e3e42"/>
          </linearGradient>
        </defs>
        <polygon points="0,0 96,0 96,92 48,72 0,92" fill="url(#navTab)"/>
        <polyline points="4,0 4,86 48,68 92,86 92,0" fill="none" stroke="#e9b7bd" stroke-width="1"/>
      </svg>
      <a class="nav-link is-active" href="#">Collection</a>
      <a class="nav-link nav-news" href="#">News</a>
      <a class="nav-link nav-about" href="#">About</a>
    </nav>

    <aside class="specials">
      <svg width="208" height="396" viewBox="0 0 208 396" aria-hidden="true">
        <defs>
          <linearGradient id="ribbonFill" x1="0" y1="0" x2="0" y2="1">
            <stop offset="0" stop-color="#5e5e62"/><stop offset="1" stop-color="#3a3a3e"/>
          </linearGradient>
        </defs>
        <polygon points="0,0 208,0 208,396 104,356 0,396" fill="url(#ribbonFill)" opacity=".93"/>
        <polyline points="6,0 6,386 104,348 202,386 202,0" fill="none" stroke="#e9b7bd" stroke-width="1"/>
      </svg>
      <h2 class="specials-title">CALLOWAY SPECIALS</h2>
      <ul class="specials-list">
        <li>Winter Collection<br>2011</li>
        <li>Spring Collection<br>2011</li>
        <li>Summer Collection<br>2012</li>
      </ul>
    </aside>

    <section class="slider">
      <div class="slide-photo" role="img" aria-label="Slide photograph of legs in sheer black stockings with a lace ribbon pattern and black peep-toe heels"></div>
      <svg class="slider-arrow prev" viewBox="0 0 29 30" aria-hidden="true">
        <rect width="29" height="30" fill="rgba(255,255,255,.7)" stroke="#e9b7bd"/>
        <polyline points="18,7 11,15 18,23" fill="none" stroke="#d9a1a8" stroke-width="1.5"/>
      </svg>
      <svg class="slider-arrow next" viewBox="0 0 29 30" aria-hidden="true">
        <rect width="29" height="30" fill="rgba(255,255,255,.7)" stroke="#e9b7bd"/>
        <polyline points="11,7 18,15 11,23" fill="none" stroke="#d9a1a8" stroke-width="1.5"/>
      </svg>
      <div class="slider-dots"><span class="is-current"></span><span></span><span></span><span></span><span></span></div>
    </section>
  </div>

  <footer class="site-footer">
    <p class="delivery">One Day Delivery<br>in the Metro Area</p>
    <ul class="footer-links links-site">
      <li><a href="#">Collection</a></li><li><a href="#">News</a></li><li><a href="#">About</a></li>
    </ul>
    <ul class="footer-links links-shop">
      <li><a href="#">Shopping Cart</a></li><li><a href="#">Shipping</a></li><li><a href="#">Returns</a></li>
    </ul>
    <ul class="footer-links links-info">
      <li><a href="#">Privacy Policy</a></li><li><a href="#">Site Map</a></li><li><a href="#">Contact</a></li>
    </ul>
    <div class="footer-brand">
      <div class="name">Calloway</div>
      <div class="tagline">Signature Italian Stockings</div>
      <div class="copyright">© Copyright 2012 Calloway Hosiery</div>
    </div>
  </footer>
</body>
</html>
```